Varlowe Supply Partners
Business Cards and Stationary
Project: Varlowe Supply Partners
Varlowe Supply Partners -
Creative Brief
Professional
Daniel Varlowe
Manufacturer's Representative
20375 82nd Lane NW Elk Ridge, MN 55492
dvarlowe@varlowesupply-example.com
www.varlowesupply-example.com

```html
<!DOCTYPE html>
<html lang="en">
<head>
<meta charset="utf-8">
<title>Varlowe Supply Partners – Business Cards</title>
<link href="https://fonts.googleapis.com/css2?family=Cinzel:wght@500&family=Source+Sans+3:wght@400;600&display=swap" rel="stylesheet">
<style>
  :root {
    --backdrop: #e9e6e1;
    --card: #ffffff;
    --ink: #3a3f4a;
    --brand-blue: #1f6fb2;
    --brand-navy: #233a6e;
    --wave-light: #5fc4ea;
    --wave-deep: #1a6db5;
    --label-blue: #2b8fd0;
    --on-wave: #ffffff;
  }
  * { margin: 0; padding: 0; box-sizing: border-box; }
  html, body { width: 1200px; height: 463px; overflow: hidden; }
  body {
    background: var(--backdrop);
    font-family: "Source Sans 3", sans-serif;
    color: var(--ink);
    position: relative;
  }
  .card {
    position: absolute;
    top: 72px;
    width: 510px;
    height: 322px;
    background: var(--card);
    border-radius: 20px;
    overflow: hidden;
    box-shadow: 0 4px 14px rgba(0,0,0,0.18);
  }
  .card--front { left: 100px; }
  .card--back { left: 640px; }
  .card__wave { position: absolute; inset: 0; width: 100%; height: 100%; }
  .brand {
    position: absolute;
    display: flex;
    align-items: center;
    gap: 14px;
  }
  .card--front .brand { left: 34px; top: 34px; }
  .card--back .brand { left: 34px; top: 40px; }
  .brand__dot {
    width: 52px; height: 52px;
    border-radius: 50%;
    background: var(--brand-blue);
    flex: none;
  }
  .brand__name {
    font-family: "Cinzel", serif;
    font-weight: 500;
    color: var(--brand-navy);
    font-size: 30px;
    line-height: 1;
    letter-spacing: 0.5px;
  }
  .brand__name span { display: block; font-size: 22px; margin-top: 6px; letter-spacing: 0.3px; }
  .contact {
    position: absolute;
    left: 36px;
    top: 140px;
    font-size: 11.5px;
    line-height: 1.55;
  }
  .contact__address { margin-bottom: 10px; }
  .contact__label { color: var(--label-blue); font-weight: 600; margin-right: 4px; }
  .person {
    position: absolute;
    right: 40px;
    bottom: 34px;
    color: var(--on-wave);
    text-align: left;
  }
  .person__name { font-size: 15px; text-transform: uppercase; letter-spacing: 0.5px; }
  .person__title { font-size: 11px; }
  .site {
    position: absolute;
    right: 38px;
    bottom: 30px;
    color: var(--on-wave);
    font-size: 12.5px;
  }
</style>
</head>
<body>
  <section class="card card--front">
    <svg class="card__wave" viewBox="0 0 510 322" preserveAspectRatio="none" aria-hidden="true">
      <defs>
        <linearGradient id="waveFront" x1="0" y1="0" x2="1" y2="0">
          <stop offset="0" stop-color="#a8e2f6"/>
          <stop offset="0.45" stop-color="var(--wave-light)"/>
          <stop offset="1" stop-color="var(--wave-deep)"/>
        </linearGradient>
      </defs>
      <path d="M0,285 C170,285 350,250 510,165 L510,322 L0,322 Z" fill="url(#waveFront)"/>
      <path d="M0,300 C180,305 360,285 510,245 L510,322 L0,322 Z" fill="var(--wave-deep)" opacity="0.55"/>
      <path d="M0,312 C160,318 340,312 510,290 L510,322 L0,322 Z" fill="var(--brand-navy)"/>
    </svg>
    <div class="brand">
      <div class="brand__dot"></div>
      <div class="brand__name">VARLOWE<span>Supply Partners</span></div>
    </div>
    <div class="contact">
      <p class="contact__address">20375 82nd Lane NW Elk Ridge, MN 55492</p>
      <p><span class="contact__label">P :</span>763.555.0142</p>
      <p><span class="contact__label">F :</span>763.555.0187</p>
      <p><span class="contact__label">E :</span>dvarlowe@varlowesupply-example.com</p>
      <p><span class="contact__label">W:</span>www.varlowesupply-example.com</p>
    </div>
    <div class="person">
      <p class="person__name">Daniel Varlowe</p>
      <p class="person__title">Manufacturer's Representative</p>
    </div>
  </section>

  <section class="card card--back">
    <svg class="card__wave" viewBox="0 0 510 322" preserveAspectRatio="none" aria-hidden="true">
      <defs>
        <linearGradient id="waveBack" x1="0" y1="0" x2="1" y2="0">
          <stop offset="0" stop-color="#a8e2f6"/>
          <stop offset="0.45" stop-color="var(--wave-light)"/>
          <stop offset="1" stop-color="var(--wave-deep)"/>
        </linearGradient>
      </defs>
      <path d="M0,270 C170,272 350,235 510,150 L510,322 L0,322 Z" fill="url(#waveBack)"/>
      <path d="M0,295 C180,300 360,280 510,235 L510,322 L0,322 Z" fill="var(--wave-deep)" opacity="0.55"/>
      <path d="M0,310 C160,316 340,310 510,286 L510,322 L0,322 Z" fill="var(--brand-navy)"/>
    </svg>
    <div class="brand">
      <div class="brand__dot"></div>
      <div class="brand__name">VARLOWE<span>Supply Partners</span></div>
    </div>
    <p class="site">www.varlowesupply-example.com</p>
  </section>
</body>
</html>
```